Skin care manufacturer looking for packaging design for new skin care brand.

We need a design and logo for a skin care brand to be sold at retail stores and online in the United States and Europe. The design will be for 1.7oz - 2oz serums that will not have a retail box. The name of the brand is Velvet Meadow and should be a luxurious brand that is approachable. The brand will consist of 4 face serums - Vitamin C, Collagen, Retinol and Hyaluronic Acid. Images shown are for inspiration only. Color of bottles can be varied based on design and bottles can be screen printed or labeled.
Updates

Need extra days to review

Target Market(s)

Target market is 30+ female

Industry/Entity Type

Beauty

Requirements
Must have
• Ingredient call outs + benefit. Ex: Vitamin C Brightening Serum. Packaging should be translucent

```html
<!DOCTYPE html>
<html lang="en">
<head>
<meta charset="utf-8">
<title>Velvet Meadow Serum Labels</title>
<link href="https://fonts.googleapis.com/css2?family=Inter:wght@400;500&display=swap" rel="stylesheet">
<style>
  :root {
    --bg: #e6e6e6;
    --silver-dark: #b9b9b9;
    --silver-mid: #d9d9d9;
    --silver-light: #f7f7f7;
    --ink: #1c1c1c;
    --rule-hydrate: #141414;
    --rule-bright: #e2631f;
  }
  * { margin: 0; padding: 0; box-sizing: border-box; }
  html, body { width: 1200px; height: 900px; overflow: hidden; }
  body {
    background: var(--bg);
    font-family: "Inter", Arial, sans-serif;
    color: var(--ink);
    position: relative;
  }
  .label-set {
    position: absolute;
    inset: 0;
    display: flex;
    justify-content: center;
    align-items: center;
    gap: 140px;
  }
  .serum-label {
    position: relative;
    width: 360px;
    height: 470px;
    background: linear-gradient(90deg,
      var(--silver-dark) 0%,
      var(--silver-light) 12%,
      var(--silver-mid) 26%,
      var(--silver-light) 42%,
      var(--silver-light) 58%,
      var(--silver-mid) 74%,
      var(--silver-light) 88%,
      var(--silver-dark) 100%);
    padding: 68px 0 0 40px;
  }
  .brand-name {
    font-weight: 400;
    font-size: 36px;
    letter-spacing: -0.5px;
    line-height: 1;
  }
  .brand-rule {
    width: 270px;
    height: 3px;
    margin: 12px 0 14px;
  }
  .serum-label--hydrate .brand-rule { background: var(--rule-hydrate); }
  .serum-label--bright .brand-rule { background: var(--rule-bright); }
  .product-name {
    font-weight: 400;
    font-size: 28px;
    line-height: 1.1;
    letter-spacing: 0.3px;
    text-transform: uppercase;
  }
  .benefits {
    position: absolute;
    left: 40px;
    top: 300px;
    list-style: none;
    font-size: 15px;
    line-height: 26px;
  }
  .volume {
    position: absolute;
    left: 0;
    right: 0;
    bottom: 42px;
    text-align: center;
    font-size: 15px;
    letter-spacing: 0.3px;
    padding-left: 20px;
  }
</style>
</head>
<body>
  <main class="label-set">
    <section class="serum-label serum-label--hydrate">
      <h1 class="brand-name">Velvet Meadow</h1>
      <div class="brand-rule"></div>
      <h2 class="product-name">Hyaluronic<br>Acid<br>Serum</h2>
      <ul class="benefits">
        <li>Deep moisturizing</li>
        <li>Improving skin elasticity</li>
      </ul>
      <p class="volume">50ML/1.7 FL. OZ.</p>
    </section>
    <section class="serum-label serum-label--bright">
      <h1 class="brand-name">Velvet Meadow</h1>
      <div class="brand-rule"></div>
      <h2 class="product-name">Vitamin C<br>Brightening<br>Serum</h2>
      <ul class="benefits">
        <li>Anti-Aging</li>
        <li>Antioxidant</li>
      </ul>
      <p class="volume">50ML/1.7 FL. OZ.</p>
    </section>
  </main>
</body>
</html>
```